Business Card / Appointment Card for Physician

On one side it should give the logo, address, and contact information, and on the other side it should br an Appointment card.

One Side:
Logo (see attached files)
Board Certified American Orthopedic Surgery

1874 Larkmoor Ave.
Suite KP7
Bronx, NY 10287
Tel: (718) 555 - 0142
Fax: (718) 555 - 0187

612 Ninth Ave.
Suite 42
New York, NY 10089
Tel: (212) 555 - 0163

Second Side:
Appointment
give them a choice of Bronx or Mahattan office
For:
Date:
Time:

If you are unable to keep your appointment, please call (718) 555-0129 24hrs in advance.

Target Market(s)

People that need orthopedic surgery

Industry/Entity Type

Business

Contact Information for Business Card

smart and attractive

Requirements
Must have
• logo
• contact information on one side, appointment information on the other

```html
<!DOCTYPE html>
<html lang="en">
<head>
<meta charset="utf-8">
<title>Dorian K. Whitfield MD PC — Business &amp; Appointment Card</title>
<link rel="stylesheet" href="https://fonts.googleapis.com/css2?family=Open+Sans:wght@400;600;700&display=swap">
<style>
  :root {
    --bg: #e4e5e7;
    --card-white: #ffffff;
    --ink: #1e1e1e;
    --brand-blue: #1f5a96;
    --brand-green: #6cbf3f;
    --green-deep: #5aae31;
    --green-light: #7ccb4f;
    --rule-green: #62b338;
    --paper-shadow: rgba(0,0,0,0.18);
  }
  * { box-sizing: border-box; margin: 0; padding: 0; }
  html, body { width: 1200px; height: 1000px; overflow: hidden; }
  body {
    background: var(--bg);
    font-family: "Open Sans", Arial, sans-serif;
    color: var(--ink);
    position: relative;
  }

  .card {
    position: absolute;
    width: 540px;
    height: 308px;
    border-radius: 3px;
    box-shadow: 0 8px 22px var(--paper-shadow);
    overflow: hidden;
  }

  /* ---------- Contact side ---------- */
  .card--contact {
    left: 625px;
    top: 170px;
    background: var(--card-white);
  }
  .brand {
    position: absolute;
    top: 34px;
    right: 40px;
    display: flex;
    align-items: center;
    gap: 10px;
  }
  .brand__dot {
    width: 22px;
    height: 22px;
    border-radius: 50%;
    background: var(--brand-blue);
  }
  .brand__name {
    font-weight: 600;
    font-size: 19px;
    color: var(--brand-blue);
    letter-spacing: 0.3px;
  }
  .rule {
    position: absolute;
    height: 3px;
    background: var(--rule-green);
  }
  .rule--left { left: 0; top: 26px; width: 110px; }
  .rule--right { right: 0; top: 160px; width: 120px; }
  .tagline {
    position: absolute;
    left: 30px;
    top: 90px;
    font-weight: 700;
    font-size: 16px;
    letter-spacing: 0.6px;
    text-transform: uppercase;
  }
  .office {
    position: absolute;
    font-size: 14.5px;
    line-height: 1.35;
  }
  .office--bronx { left: 30px; top: 124px; }
  .office--manhattan { right: 40px; top: 196px; text-align: right; }

  /* ---------- Appointment side ---------- */
  .card--appointment {
    left: 40px;
    top: 470px;
    background: linear-gradient(135deg, var(--green-light), var(--green-deep));
    color: #ffffff;
  }
  .card__art {
    position: absolute;
    inset: 0;
    background: radial-gradient(ellipse at 55% 45%, rgba(255,255,255,0.12), rgba(255,255,255,0) 65%);
  }
  .appt__choice {
    position: absolute;
    display: flex;
    align-items: center;
    gap: 12px;
    font-size: 15px;
  }
  .appt__choice--bronx { left: 28px; top: 24px; }
  .appt__choice--manhattan { right: 34px; top: 116px; }
  .checkbox {
    width: 24px;
    height: 24px;
    background: #ffffff;
  }
  .appt__title {
    position: absolute;
    left: 0; right: 0;
    top: 70px;
    text-align: center;
    font-weight: 700;
    font-size: 17px;
    letter-spacing: 1px;
    text-transform: uppercase;
  }
  .field {
    position: absolute;
    left: 28px;
    right: 28px;
    border-bottom: 1.5px solid #ffffff;
    font-size: 14.5px;
    padding-bottom: 3px;
  }
  .field--for { top: 150px; }
  .field--date { top: 190px; width: 250px; right: auto; }
  .field--time { top: 190px; left: 290px; }
  .appt__note {
    position: absolute;
    left: 28px;
    right: 28px;
    top: 240px;
    font-size: 13px;
    line-height: 1.4;
    text-transform: uppercase;
    letter-spacing: 0.3px;
  }
  .appt__note strong { font-weight: 700; }

  /* ---------- Brand lockup ---------- */
  .lockup {
    position: absolute;
    right: 60px;
    bottom: 70px;
    display: flex;
    align-items: center;
    gap: 12px;
  }
  .lockup__dot {
    width: 34px;
    height: 34px;
    border-radius: 50%;
    background: var(--brand-blue);
  }
  .lockup__name {
    font-weight: 600;
    font-size: 26px;
    color: var(--brand-blue);
    letter-spacing: 0.4px;
  }
</style>
</head>
<body>

  <section class="card card--contact" aria-label="Contact side">
    <span class="rule rule--left"></span>
    <div class="brand">
      <span class="brand__dot"></span>
      <span class="brand__name">DORIAN K. WHITFIELD MD PC</span>
    </div>
    <h1 class="tagline">Board Certified American Orthopedic Surgery</h1>
    <address class="office office--bronx" style="font-style:normal">
      1874 Larkmoor Ave.<br>
      Suite KP7<br>
      Bronx, NY 10287<br>
      T: (718) 555 - 0142<br>
      F: (718) 555 - 0187
    </address>
    <span class="rule rule--right"></span>
    <address class="office office--manhattan" style="font-style:normal">
      612 Ninth Ave.<br>
      Suite 42<br>
      New York, NY 10089<br>
      T: (212) 555 - 0163
    </address>
  </section>

  <section class="card card--appointment" aria-label="Appointment side">
    <div class="card__art" role="img" aria-label="Faint line illustration of knee and shoulder anatomy"></div>
    <label class="appt__choice appt__choice--bronx"><span class="checkbox"></span>Bronx Office</label>
    <h2 class="appt__title">Appointment</h2>
    <label class="appt__choice appt__choice--manhattan"><span class="checkbox"></span>Mahattan Office</label>
    <div class="field field--for">For:</div>
    <div class="field field--date">Date:</div>
    <div class="field field--time">Time:</div>
    <p class="appt__note">If you are unable to keep your appointment,<br>please call <strong>(718) 555-0129</strong> 24hrs in advance.</p>
  </section>

  <div class="lockup">
    <span class="lockup__dot"></span>
    <span class="lockup__name">DORIAN K. WHITFIELD MD PC</span>
  </div>

</body>
</html>
```